The Lantern Protocol: A Practical Guide for Tending Old Orchards

This will be for both the hard cover and paperback version. A core theme of the book and what we want to cover to convey is the journey or transformation to "happiness". Concepts such as road/pathway, mountain top, sunrise, dark to bright colors, out-of-focus to in-focus, clouds parting, etc., all represent this idea. I am attaching a 1-page book summary for more information. I like the idea of the subtitle being in a gold seal, but that is not necessary. I am open to any designs, but it should at least be conceptually related to the book.

```html
<!DOCTYPE html>
<html lang="en">
<head>
<meta charset="utf-8">
<title>The Lantern Protocol — Book Cover</title>
<link rel="stylesheet" href="https://fonts.googleapis.com/css2?family=Bebas+Neue&family=Montserrat:wght@700;800&display=swap">
<style>
  :root {
    --page-bg: #ffffff;
    --gold-deep: #8a5810;
    --gold-mid: #a7731f;
    --gold-light: #c9a064;
    --title-white: #ffffff;
    --title-yellow: #f7e733;
    --band-gold-1: #d6a548;
    --band-gold-2: #f6dc8c;
    --band-gold-3: #c8923a;
    --author-ink: #111111;
    --seal-ink: #141414;
    --photo-warm: #b99a7c;
    --photo-cool: #6f6a64;
  }
  * { margin: 0; padding: 0; box-sizing: border-box; }
  html, body {
    width: 1200px;
    height: 1200px;
    overflow: hidden;
    background: var(--page-bg);
  }
  .book-cover {
    position: absolute;
    left: 240px;
    top: 60px;
    width: 720px;
    height: 1080px;
    overflow: hidden;
  }
  .cover-top {
    position: absolute;
    inset: 0 0 auto 0;
    height: 562px;
    background: linear-gradient(125deg, var(--gold-mid) 0%, var(--gold-deep) 38%, var(--gold-mid) 70%, var(--gold-light) 100%);
  }
  .title {
    font-family: "Bebas Neue", "Oswald", sans-serif;
    font-weight: 400;
    color: var(--title-white);
  }
  .title-line {
    position: absolute;
    left: 44px;
    display: block;
    line-height: 1;
    letter-spacing: 2px;
    white-space: nowrap;
  }
  .title-line--the { top: 147px; font-size: 147px; }
  .title-line--accent { top: 264px; font-size: 183px; color: var(--title-yellow); }
  .title-line--last { top: 412px; font-size: 154px; }
  .seal {
    position: absolute;
    left: 315px;
    top: 28px;
    width: 240px;
    height: 240px;
  }
  .seal svg { position: absolute; inset: 0; }
  .seal-text {
    position: absolute;
    inset: 62px 44px;
    display: flex;
    align-items: center;
    justify-content: center;
    text-align: center;
    font-family: "Montserrat", Arial, sans-serif;
    font-weight: 800;
    font-size: 19px;
    line-height: 22px;
    color: var(--seal-ink);
  }
  .cover-photo {
    position: absolute;
    left: 0;
    top: 562px;
    width: 720px;
    height: 401px;
    background:
      radial-gradient(ellipse at 75% 30%, #e8d6c0 0%, transparent 55%),
      linear-gradient(180deg, var(--photo-warm) 0%, #8f8478 55%, var(--photo-cool) 100%);
  }
  .author-band {
    position: absolute;
    left: 0;
    bottom: 0;
    width: 720px;
    height: 117px;
    background: linear-gradient(90deg, var(--band-gold-1) 0%, var(--band-gold-2) 45%, var(--band-gold-3) 100%);
    display: flex;
    align-items: center;
    justify-content: center;
  }
  .author-name {
    font-family: "Montserrat", Arial, sans-serif;
    font-weight: 800;
    font-size: 54px;
    letter-spacing: 1px;
    color: var(--author-ink);
  }
</style>
</head>
<body>
  <main class="book-cover">
    <section class="cover-top">
      <h1 class="title">
        <span class="title-line title-line--the">THE</span>
        <span class="title-line title-line--accent">LANTERN</span>
        <span class="title-line title-line--last">PROTOCOL</span>
      </h1>
      <div class="seal">
        <svg viewBox="-120 -120 240 240" width="240" height="240" aria-hidden="true">
          <defs>
            <linearGradient id="sealRim" x1="0" y1="0" x2="1" y2="1">
              <stop offset="0" stop-color="#f7e39a"/>
              <stop offset="0.5" stop-color="#c99a3a"/>
              <stop offset="1" stop-color="#f0d27a"/>
            </linearGradient>
            <radialGradient id="sealFace" cx="0.4" cy="0.35" r="0.75">
              <stop offset="0" stop-color="#fbeaa6"/>
              <stop offset="0.6" stop-color="#e2b65a"/>
              <stop offset="1" stop-color="#b9862c"/>
            </radialGradient>
          </defs>
          <g fill="url(#sealRim)">
            <rect x="-85" y="-85" width="170" height="170" transform="rotate(0)"/>
            <rect x="-85" y="-85" width="170" height="170" transform="rotate(10)"/>
            <rect x="-85" y="-85" width="170" height="170" transform="rotate(20)"/>
            <rect x="-85" y="-85" width="170" height="170" transform="rotate(30)"/>
            <rect x="-85" y="-85" width="170" height="170" transform="rotate(40)"/>
            <rect x="-85" y="-85" width="170" height="170" transform="rotate(50)"/>
            <rect x="-85" y="-85" width="170" height="170" transform="rotate(60)"/>
            <rect x="-85" y="-85" width="170" height="170" transform="rotate(70)"/>
            <rect x="-85" y="-85" width="170" height="170" transform="rotate(80)"/>
          </g>
          <circle r="98" fill="url(#sealFace)" stroke="#fff2c0" stroke-width="2"/>
          <circle r="90" fill="none" stroke="#b07d26" stroke-width="1.5" stroke-dasharray="2 3"/>
        </svg>
        <p class="seal-text">A Practical Guide for Tending Old Orchards</p>
      </div>
    </section>

    <div class="cover-photo" role="img" aria-label="Photograph: a boy handing a wrapped gift to a smiling grandfather on a sofa in a warm living room"></div>

    <footer class="author-band">
      <p class="author-name">DANA R. WHITFIELD</p>
    </footer>
  </main>
</body>
</html>
```